Beer Bottle Label

We are a boutique brewery. We need to design beer bottle labels. Our image theme so far has incorporated oil paintings from an Australian artist, and we would like to continue this theme. I will attach a demo label that I made (it's terrible!), and the image we would like to incorporate in the first design. I will also attach an image of the beer tap badge. We would like a label shaped like the demo I provide, or a rectangular label 8cm high * 15cm long. We are looking for a 'classy' label. The label also needs to incorporate our business logo, which I have attached. The Label must also include, in small writing: '4.5%abv' and 'contains approx. 1.2 standard drinks' and '330mL' and 'Brewed by Fenwary Ales. 48 Pellam Road, Durnside Victoria Australia 3279'.
If we receive an acceptable design from ArtHively, we would like you to design our other bottle labels, and redesign our beer tap badges.

Target Market(s)

Australian craft beer consumers

Industry/Entity Type

Boutique

Requirements
Must have
• Legal requirements: '4.5%abv' and 'contains approx. 1.2 standard drinks' and '330mL' and 'Brewed by Fenwary Ales. 48 Pellam Road, Durnside Victoria Australia 3279'
• Our business logo (see attached file).
• Must also utilise the painting (see attached file)

```html
<!DOCTYPE html>
<html lang="en">
<head>
<meta charset="utf-8">
<title>Durnside Draught – Bottle Label</title>
<link href="https://fonts.googleapis.com/css2?family=Oswald:wght@600&family=EB+Garamond:wght@400;500&family=Mrs+Saint+Delafield&family=Montserrat:wght@700&display=swap" rel="stylesheet">
<style>
  :root {
    --page: #f1f1ef;
    --ink: #2b2417;
    --gold: #8a7a4e;
    --gold-light: #a8955c;
    --neck: #1d1c1b;
    --white: #ffffff;
    --paint-green: #6f7a4a;
    --paint-ochre: #b98a3a;
    --paint-rust: #8a4a26;
    --paint-mist: #c9c3a4;
  }
  * { margin: 0; padding: 0; box-sizing: border-box; }
  html, body { width: 1200px; height: 1200px; overflow: hidden; background: var(--page); }
  .canvas { position: relative; width: 1200px; height: 1200px; }

  /* neck label */
  .neck-label { position: absolute; left: 590px; top: 202px; width: 372px; height: 206px; }
  .neck-label svg { position: absolute; inset: 0; }
  .neck-text { position: absolute; left: 0; right: 0; top: 50px; text-align: center; color: var(--gold); }
  .neck-text .product { font-family: 'Oswald', sans-serif; font-weight: 600; font-size: 29px; line-height: 0.98; letter-spacing: 0.5px; }
  .neck-text .style { font-family: 'Mrs Saint Delafield', cursive; font-size: 20px; line-height: 1.1; margin-top: 1px; }
  .neck-text .brand { font-family: 'EB Garamond', serif; font-size: 13px; letter-spacing: 0.8px; line-height: 1.1; }
  .neck-text .brand-sub { font-family: 'EB Garamond', serif; font-size: 5.5px; letter-spacing: 0.5px; line-height: 1.3; }

  /* main label */
  .body-label { position: absolute; left: 162px; top: 449px; width: 874px; height: 464px; overflow: hidden; box-shadow: 0 2px 6px rgba(0,0,0,0.12); }
  .painting {
    position: absolute; inset: 0;
    background:
      radial-gradient(ellipse 40% 30% at 45% 20%, var(--paint-mist) 0%, transparent 70%),
      radial-gradient(ellipse 35% 40% at 40% 75%, var(--paint-ochre) 0%, transparent 70%),
      radial-gradient(ellipse 25% 30% at 30% 60%, var(--paint-rust) 0%, transparent 75%),
      linear-gradient(160deg, #8d9465 0%, var(--paint-green) 35%, #9a7a3c 70%, #7a4f22 100%);
  }
  .cartouche { position: absolute; left: 446px; top: 92px; width: 340px; height: 280px; }
  .cartouche svg { position: absolute; inset: 0; }
  .cartouche-text { position: absolute; left: 0; right: 0; top: 42px; text-align: center; color: var(--ink); }
  .mark { width: 28px; height: 28px; border-radius: 50%; background: var(--paint-green); margin: 0 auto 10px; }
  .cartouche-text .product { font-family: 'Oswald', sans-serif; font-weight: 600; font-size: 44px; line-height: 0.98; }
  .cartouche-text .style { font-family: 'Mrs Saint Delafield', cursive; font-size: 24px; line-height: 1; margin-top: 2px; }
  .cartouche-text .brand { font-family: 'EB Garamond', serif; font-size: 15px; letter-spacing: 1px; color: var(--gold); margin-top: 4px; }
  .cartouche-text .brand-sub { font-family: 'EB Garamond', serif; font-size: 6.5px; letter-spacing: 0.4px; color: var(--gold); line-height: 1.3; }

  .legal { position: absolute; left: 446px; width: 340px; top: 382px; text-align: center; color: var(--white); }
  .legal .abv { font-family: 'Montserrat', sans-serif; font-weight: 700; font-size: 13px; }
  .legal .drinks { font-family: 'EB Garamond', serif; font-variant: small-caps; font-size: 11.5px; letter-spacing: 1px; }
  .legal .brewer { font-family: 'EB Garamond', serif; font-style: italic; font-size: 11.5px; letter-spacing: 0.3px; }
</style>
</head>
<body>
<main class="canvas">

  <section class="neck-label">
    <svg viewBox="0 0 372 206" width="372" height="206" aria-hidden="true">
      <path d="M16 0 H356 L372 170 H246 A70 70 0 0 1 126 170 H0 Z" fill="var(--neck)"/>
    </svg>
    <div class="neck-text">
      <div class="product">DURNSIDE<br>DRAUGHT</div>
      <div class="style">craft beer</div>
      <div class="brand">THE MARROWGUM</div>
      <div class="brand-sub">BREWERY AND DISTILLERY<br>DURNSIDE, VICTORIA</div>
    </div>
  </section>

  <section class="body-label">
    <div class="painting" role="img" aria-label="Oil painting of bullock drivers and horses hauling a log through golden bushland, with a steam train crossing a trestle bridge behind"></div>

    <div class="cartouche">
      <svg viewBox="0 0 340 280" width="340" height="280" aria-hidden="true">
        <path d="M40 70 Q70 70 80 45 Q170 0 260 45 Q270 70 300 70 Q340 140 300 210 Q270 210 260 235 Q170 280 80 235 Q70 210 40 210 Q0 140 40 70 Z" fill="var(--gold)"/>
        <g transform="translate(170 140) scale(0.93) translate(-170 -140)">
          <path d="M40 70 Q70 70 80 45 Q170 0 260 45 Q270 70 300 70 Q340 140 300 210 Q270 210 260 235 Q170 280 80 235 Q70 210 40 210 Q0 140 40 70 Z" fill="var(--white)"/>
        </g>
        <g transform="translate(170 140) scale(0.89) translate(-170 -140)">
          <path d="M40 70 Q70 70 80 45 Q170 0 260 45 Q270 70 300 70 Q340 140 300 210 Q270 210 260 235 Q170 280 80 235 Q70 210 40 210 Q0 140 40 70 Z" fill="none" stroke="#9a9a9a" stroke-width="1" stroke-dasharray="2 2"/>
        </g>
      </svg>
      <div class="cartouche-text">
        <div class="mark"></div>
        <div class="product">DURNSIDE<br>DRAUGHT</div>
        <div class="style">craft beer</div>
        <div class="brand">THE MARROWGUM</div>
        <div class="brand-sub">BREWERY AND DISTILLERY<br>DURNSIDE, VICTORIA</div>
      </div>
    </div>

    <div class="legal">
      <div class="abv">4.5% abv. 330ml</div>
      <div class="drinks">Contains approx. 1.2 std drinks</div>
      <div class="brewer">Fenwary Ales. 48 Pellam Rd, Durnside Vic 3279</div>
    </div>
  </section>

</main>
</body>
</html>
```